Core Values poster for our office wall

We have a set of core values in our business and we want to create a nice looking poster to go up on our office wall.

Probably either A1 or A0 sizing.

It is important that the poster represents us as a company and our values.
You can get some ideas on us via the website colours/layout etc - www.marlowbrook.com.au

We need it to communicate our Values and how we love having a fun and encouraging environment.

Values: (which also spell out INSPIRED)
And some sub words related to that one

Initative - Ownership, accountability, innovation
Nurturing - Relationships, Community, Helpful
Success - Empowered
Passion - Fun, Relaxed
Integrity - Trust, Honesty, Respectful, Fortitude
Results - Knowledge, Confidence, Go-getter
Efficiency - Consistent, Organised, Fanatic Discipline
Dependability - Predictability, Security, Responsive, Execution

The below link contains some copies of our logo and also various ones of our company mascot.

https://marlowbrook.filequaybox.com/_layouts/15/guestaccess.aspx?folderid=4d21b8f07c3ea5d611b82af07e4813c9e&authkey=KqwTRmzo3pLdXc72yyHJ-Rk&e=9P2TdQ
Updates

Sorry everyone, A question made me realise I had left out the sub words to each of the main words. Here is an update. Initative - Ownership, accountability, innovation Nurturing - Relationships, Community, Helpful Success - Empowered Passion - Fun, Relaxed Integrity - Trust, Honesty, Respectful, Fortitude Results - Knowledge, Confidence, Go-getter Efficiency - Consistent, Organised, Fanatic Discipline Dependability - Predictability, Security, Responsive, Execution

Industry/Entity Type

Business

Requirements
Must have
• Good clean clear design
• Represent our company branding

```html
<!DOCTYPE html>
<html lang="en">
<head>
<meta charset="utf-8">
<title>Marlow Brook – Core Values Poster</title>
<link rel="stylesheet" href="https://fonts.googleapis.com/css2?family=Open+Sans:wght@400;700&family=Oswald:wght@600&display=swap">
<style>
  :root {
    --cream: #fffff4;
    --mist: #c9cedd;
    --navy: #1d5c95;
    --deep: #1c5b9a;
    --ocean: #2069a8;
    --sky: #00b4ee;
    --badge: #6ccff6;
    --subword: #3cbaf2;
    --white: #ffffff;
    --frame: #a8d8f0;
    --mascot-light: #5cc0f0;
    --mascot-dark: #1f7cc0;
  }
  * { margin: 0; padding: 0; box-sizing: border-box; }
  html, body { width: 848px; height: 1200px; overflow: hidden; }
  body {
    position: relative;
    font-family: "Open Sans", Arial, sans-serif;
    background: linear-gradient(to bottom,
      var(--cream) 0%, var(--cream) 44%, var(--mist) 53%,
      #4a6497 58.5%, var(--deep) 63%, var(--ocean) 73%,
      #1d63a3 80%, #0f8fd0 93%, var(--sky) 100%);
  }
  .poster-frame {
    position: absolute; left: 48px; top: 52px; width: 751px; height: 1092px;
    border: 1px dashed var(--frame);
  }
  .guide {
    position: absolute; left: 48px; width: 751px; height: 0;
    border-top: 1px dashed var(--frame); opacity: .7;
  }
  .guide--top { top: 724px; }
  .guide--bottom { top: 935px; }

  .mascot {
    position: absolute; left: 200px; top: 100px; width: 446px; height: 522px;
    border-radius: 36px;
    background: linear-gradient(to bottom, var(--mascot-light), var(--mascot-dark));
  }
  .mascot__name {
    position: absolute; left: 0; right: 0; top: 386px;
    text-align: center; font-weight: 700; font-size: 32px;
    color: var(--navy); letter-spacing: .5px;
  }

  .value { position: absolute; width: 180px; }
  .value__badge {
    width: 96px; height: 96px; border-radius: 50%;
    background: var(--navy);
    display: flex; align-items: center; justify-content: center;
    margin-left: -15px;
  }
  .value__letter {
    width: 66px; height: 66px; border-radius: 50%;
    background: var(--badge);
    color: var(--white);
    font-family: "Oswald", "Arial Narrow", sans-serif;
    font-weight: 600; font-size: 42px; line-height: 66px; text-align: center;
  }
  .value__title {
    margin-top: 5px;
    color: var(--white); font-weight: 700; font-size: 15.5px; line-height: 20px;
    letter-spacing: -.3px;
  }
  .value__traits { list-style: none; }
  .value__traits li {
    color: var(--subword); font-size: 15.5px; line-height: 20.5px; letter-spacing: -.3px;
  }
  .row-1 { top: 680px; }
  .row-2 { top: 887px; }
  .col-1 { left: 106px; }
  .col-2 { left: 293px; }
  .col-3 { left: 488px; }
  .col-4 { left: 682px; }
</style>
</head>
<body>
  <div class="poster-frame"></div>
  <div class="guide guide--top"></div>
  <div class="guide guide--bottom"></div>

  <div class="mascot" role="img" aria-label="Company mascot illustration: a friendly blue monster carrying the company name on its belly">
    <div class="mascot__name">Marlow Brook</div>
  </div>

  <section class="value row-1 col-1">
    <div class="value__badge"><div class="value__letter">I</div></div>
    <h2 class="value__title">INITIATIVE</h2>
    <ul class="value__traits"><li>OWNERSHIP</li><li>ACCOUNTABILITY</li><li>INNOVATION</li></ul>
  </section>
  <section class="value row-1 col-2">
    <div class="value__badge"><div class="value__letter">N</div></div>
    <h2 class="value__title">NURTURING</h2>
    <ul class="value__traits"><li>RELATIONSHIPS</li><li>COMMUNITY</li><li>HELPFUL</li></ul>
  </section>
  <section class="value row-1 col-3">
    <div class="value__badge"><div class="value__letter">S</div></div>
    <h2 class="value__title">SUCCESS</h2>
    <ul class="value__traits"><li>EMPOWERMENT</li></ul>
  </section>
  <section class="value row-1 col-4">
    <div class="value__badge"><div class="value__letter">P</div></div>
    <h2 class="value__title">PASSION</h2>
    <ul class="value__traits"><li>FUN</li><li>RELAXED</li></ul>
  </section>

  <section class="value row-2 col-1">
    <div class="value__badge"><div class="value__letter">I</div></div>
    <h2 class="value__title">INTEGRITY</h2>
    <ul class="value__traits"><li>TRUST</li><li>HONESTY</li><li>RESPECTFUL</li><li>FORTITUDE</li></ul>
  </section>
  <section class="value row-2 col-2">
    <div class="value__badge"><div class="value__letter">R</div></div>
    <h2 class="value__title">RESULTS</h2>
    <ul class="value__traits"><li>KNOWLEDGE</li><li>CONFIDENCE</li><li>GO-GETTER</li></ul>
  </section>
  <section class="value row-2 col-3">
    <div class="value__badge"><div class="value__letter">E</div></div>
    <h2 class="value__title">EFFICIENCY</h2>
    <ul class="value__traits"><li>CONSISTENT</li><li>ORGANISED</li><li>FANATIC</li><li>DISCIPLINE</li></ul>
  </section>
  <section class="value row-2 col-4">
    <div class="value__badge"><div class="value__letter">D</div></div>
    <h2 class="value__title">DEPENDABILITY</h2>
    <ul class="value__traits"><li>PREDICTABILITY</li><li>SECURITY</li><li>RESPONSIVE</li><li>EXECUTION</li></ul>
  </section>
</body>
</html>
```